11 x 11 Flyer Design for Social Media - Reverse Mortgages

62 or older?

A Reverse Mortgage
could be
Your Road to Financial Freedom

* No Monthly Payments
* No Income Requirements
* No Credit Score Requirements
* No Loss of Ownership

Receive cash by lump sum, monthly installments or a line of credit!!

Call us today for a Free Consultation!!
(800) 471-2965

Bluegate Financial Services, Inc.
NMLS #318760
www.bluegatehome.com

```html
<!DOCTYPE html>
<html lang="en">
<head>
<meta charset="utf-8">
<title>Reverse Mortgage Flyer – Bluegate Financial Services</title>
<link href="https://fonts.googleapis.com/css2?family=Caveat+Brush&family=Roboto+Condensed:wght@300;400;700;800&family=Poppins:wght@400;500;600;700&display=swap" rel="stylesheet">
<style>
  :root {
    --navy: #0c4a7e;
    --navy-deep: #0a3f6d;
    --brand-blue: #0f5ca3;
    --ink-blue: #163f72;
    --yellow: #eeff00;
    --white: #ffffff;
    --orange: #f7a312;
    --text-dark: #333333;
  }
  * { margin: 0; padding: 0; box-sizing: border-box; }
  html, body { width: 1200px; height: 1200px; overflow: hidden; }
  body { background: var(--white); position: relative; font-family: "Poppins", sans-serif; }

  .flyer { position: absolute; inset: 0; background: var(--navy); overflow: hidden; }
  .shapes { position: absolute; inset: 0; }

  .brand {
    position: absolute; left: 97px; top: 78px;
    display: flex; align-items: center; gap: 12px;
    font-family: "Poppins", sans-serif; font-weight: 600; font-size: 21px;
    color: var(--brand-blue);
  }
  .brand-dot { width: 34px; height: 34px; border-radius: 50%; background: var(--brand-blue); }

  .headline { position: absolute; left: 83px; top: 220px; }
  .age-question {
    font-family: "Caveat Brush", cursive; color: var(--white);
    font-size: 92px; line-height: 1; margin-left: 58px;
  }
  .product {
    font-family: "Roboto Condensed", sans-serif; font-weight: 800;
    color: var(--yellow); font-size: 117px; line-height: 0.93;
    letter-spacing: -1px; margin-top: 0;
  }
  .tagline-light {
    font-family: "Roboto Condensed", sans-serif; font-weight: 400;
    color: var(--white); font-size: 51px; line-height: 1; margin-top: 14px;
  }
  .tagline-bold {
    font-family: "Roboto Condensed", sans-serif; font-weight: 700;
    color: var(--white); font-size: 51px; line-height: 1; margin-top: 12px;
  }
  .divider { position: absolute; left: 85px; top: 668px; width: 151px; height: 9px; background: var(--white); }

  .benefits { position: absolute; left: 90px; top: 690px; list-style: none; }
  .benefits li {
    display: flex; align-items: center; gap: 8px;
    color: var(--white); font-size: 23px; height: 37px;
  }
  .benefits svg { width: 22px; height: 22px; flex: none; }

  .payout {
    position: absolute; left: 91px; top: 852px;
    font-family: "Caveat Brush", cursive; color: var(--yellow);
    font-size: 37px; line-height: 47px;
  }

  .photo { position: absolute; left: 560px; top: 120px; width: 640px; height: 910px; }

  .cta-lead { position: absolute; left: 183px; top: 1073px; font-size: 17px; color: var(--text-dark); letter-spacing: 0.3px; }
  .phone { position: absolute; left: 97px; top: 1100px; display: flex; align-items: center; gap: 12px; }
  .phone-icon { width: 70px; height: 70px; }
  .phone-number { font-weight: 700; font-size: 55px; color: var(--brand-blue); letter-spacing: 1px; }

  .company-info {
    position: absolute; left: 715px; top: 1060px;
    font-weight: 500; font-size: 27px; line-height: 35px; color: var(--ink-blue);
  }
</style>
</head>
<body>
<main class="flyer">
  <div class="photo" role="img" aria-label="Photo of a smiling senior couple in white shirts, arms linked"
       style="background: radial-gradient(ellipse at 60% 55%, #f2f4f7 0%, #dfe3ea 45%, #8a5a3c 75%, rgba(12,74,126,0) 100%);"></div>

  <svg class="shapes" viewBox="0 0 1200 1200" preserveAspectRatio="none" aria-hidden="true">
    <path d="M0 0 H807 C620 115 340 215 0 206 Z" fill="var(--white)"/>
    <path d="M0 982 C260 978 480 960 690 935 C860 965 1010 1025 1200 1012 V1200 H0 Z" fill="var(--orange)"/>
    <path d="M0 996 C260 992 480 972 690 944 C860 975 1010 1020 1200 1006 V1200 H0 Z" fill="var(--white)"/>
  </svg>

  <div class="brand"><span class="brand-dot"></span>Bluegate Financial Services, Inc.</div>

  <header class="headline">
    <div class="age-question">62 or older?</div>
    <h1 class="product">A REVERSE<br>MORTGAGE</h1>
    <p class="tagline-light">COULD BE YOUR ROAD TO</p>
    <p class="tagline-bold">FINANCIAL FREEDOM</p>
  </header>
  <div class="divider"></div>

  <ul class="benefits">
    <li><svg viewBox="0 0 24 24"><circle cx="11" cy="13" r="9" fill="none" stroke="var(--yellow)" stroke-width="2"/><path d="M6 12 L11 17 L22 4" fill="none" stroke="var(--yellow)" stroke-width="2.4" stroke-linecap="round"/></svg>No Monthly Payments</li>
    <li><svg viewBox="0 0 24 24"><circle cx="11" cy="13" r="9" fill="none" stroke="var(--yellow)" stroke-width="2"/><path d="M6 12 L11 17 L22 4" fill="none" stroke="var(--yellow)" stroke-width="2.4" stroke-linecap="round"/></svg>No Income Requirements</li>
    <li><svg viewBox="0 0 24 24"><circle cx="11" cy="13" r="9" fill="none" stroke="var(--yellow)" stroke-width="2"/><path d="M6 12 L11 17 L22 4" fill="none" stroke="var(--yellow)" stroke-width="2.4" stroke-linecap="round"/></svg>No Credit Score Requirements</li>
    <li><svg viewBox="0 0 24 24"><circle cx="11" cy="13" r="9" fill="none" stroke="var(--yellow)" stroke-width="2"/><path d="M6 12 L11 17 L22 4" fill="none" stroke="var(--yellow)" stroke-width="2.4" stroke-linecap="round"/></svg>No Loss of Ownership</li>
  </ul>

  <p class="payout">Receive cash by lump sum, monthly<br>installments or a line of credit!!</p>

  <p class="cta-lead">Call us today for a Free Consultation!!</p>
  <div class="phone">
    <svg class="phone-icon" viewBox="0 0 70 70" aria-hidden="true">
      <circle cx="35" cy="35" r="35" fill="var(--brand-blue)"/>
      <path d="M24 18 c3 -2 5 -1 6 1 l3 7 c1 2 0 4 -2 5 l-2 1 c2 5 6 9 11 11 l1 -2 c1 -2 3 -3 5 -2 l7 3 c2 1 3 3 1 6 c-3 4 -7 5 -12 3 c-10 -4 -17 -11 -21 -21 c-2 -5 -1 -9 3 -12 z" fill="var(--white)"/>
    </svg>
    <span class="phone-number">(800) 471-2965</span>
  </div>

  <address class="company-info" style="font-style: normal;">
    Bluegate Financial Services, Inc.<br>
    NMLS #318760<br>
    www.bluegatehome.com
  </address>
</main>
</body>
</html>
```